Healthcare marketing Website design

This is for a healthcare marketing agency
All details and brief included in the files

I need the design to be incredible!

5 pages to be designed
Home page
About
Portfolio Page
Services
Start your project page

If you need more stock images - download preview images from kestrine pix so I can purchase at a later date

```html
<!DOCTYPE html>
<html lang="en">
<head>
<meta charset="utf-8">
<title>Northline Consulting – Healthcare Marketing</title>
<link href="https://fonts.googleapis.com/css2?family=Montserrat:wght@300;400;500;600;700&family=Quicksand:wght@400;500;600;700&display=swap" rel="stylesheet">
<style>
:root{
  --navy:#1b2d52;
  --navy-deep:#15244a;
  --blue:#0b9de4;
  --cyan:#1fa9e6;
  --sky:#e4f6fd;
  --ink:#1d2a44;
  --text:#3d4a5e;
  --white:#ffffff;
  --teal:#3fd6c0;
  --orange:#f7941d;
  --ring:#cde9f5;
}
*{margin:0;padding:0;box-sizing:border-box}
html,body{width:1200px;height:5296px;overflow:hidden}
body{position:relative;font-family:"Montserrat",sans-serif;color:var(--text);background:var(--white)}
.abs{position:absolute}
.heading{font-family:"Quicksand",sans-serif;font-weight:500;color:var(--ink);letter-spacing:.5px}
.btn{position:absolute;height:50px;border-radius:25px;display:flex;align-items:center;justify-content:center;font-size:14px;font-weight:500;letter-spacing:.4px;white-space:nowrap}
.btn-cyan{background:var(--cyan);color:var(--white)}
.btn-navy{background:var(--navy);color:var(--white)}
.btn-white{background:var(--white);color:var(--navy)}
.photo{position:absolute}
.tint-block{position:absolute}

/* header */
.site-header{position:absolute;left:0;top:0;width:1200px;height:70px;background:var(--white);z-index:2}
.brand{position:absolute;left:160px;top:12px;display:flex;align-items:center;gap:10px}
.brand-mark{width:34px;height:34px;border-radius:50%;background:var(--blue)}
.brand-name{font-family:"Quicksand",sans-serif;font-size:30px;font-weight:500;color:var(--blue);line-height:1}
.brand-sub{font-family:"Quicksand",sans-serif;font-size:10px;font-weight:500;color:var(--blue);letter-spacing:1px;margin-left:2px}
.main-nav{position:absolute;left:505px;top:26px;display:flex;gap:34px;font-size:13px;font-weight:600;color:var(--ink)}

/* hero */
.hero{position:absolute;left:0;top:70px;width:1200px;height:478px;background:linear-gradient(90deg,#eef1f4 0%,#f4f6f8 45%,#e6ecf1 100%)}
.hero-photo{left:640px;top:0;width:560px;height:478px;background:linear-gradient(90deg,rgba(230,236,241,0) 0%,#dfe6ec 30%,#f2f4f6 70%,#d8dfe6 100%)}
.hero-welcome{left:162px;top:90px;font-family:"Quicksand",sans-serif;font-size:23px;color:var(--blue)}
.hero-title{left:160px;top:118px;font-size:33px;font-weight:400}
.hero-sub{left:162px;top:162px;font-size:20px;font-weight:500;color:var(--ink)}
.hero-copy{left:162px;top:196px;width:480px;font-size:13.5px;line-height:25px;color:var(--ink)}
.hero-btn{left:162px;top:292px;width:240px;height:40px;font-size:12px;font-weight:700}
.scroll-cue{left:578px;top:522px;width:44px;height:44px;border-radius:50%;background:var(--white);box-shadow:0 2px 8px rgba(0,0,0,.12);display:flex;align-items:center;justify-content:center;z-index:2}

/* stats */
.stats{position:absolute;left:0;top:548px;width:1200px;height:597px;background:var(--sky)}
.stats-title{left:0;width:1200px;top:88px;text-align:center;font-size:34px;line-height:40px;font-weight:400}
.stats-lead{left:0;width:1200px;top:178px;text-align:center;font-size:15px;color:var(--ink)}
.stat-card{position:absolute;top:228px;width:205px;height:180px;background:var(--white);border-radius:40px 40px 80px 80px;box-shadow:0 4px 14px rgba(20,80,130,.08);text-align:center}
.stat-badge{position:absolute;left:57px;top:-2px;width:92px;height:92px;border-radius:50%;display:flex;align-items:center;justify-content:center;color:var(--white);font-family:"Quicksand",sans-serif;font-weight:700;font-size:52px;border:4px solid var(--white);box-shadow:0 3px 8px rgba(0,0,0,.12)}
.stat-badge sup{font-size:22px;vertical-align:top;line-height:40px}
.stat-text{position:absolute;left:14px;right:14px;top:110px;font-size:12px;line-height:17px;color:var(--text)}

/* mission */
.mission{position:absolute;left:0;top:1145px;width:1200px;height:748px;background:var(--navy);border-radius:260px 0 0 0}
.mission-title{left:0;width:1200px;top:108px;text-align:center;font-size:35px;line-height:50px;color:var(--white);font-weight:400}
.mission-photo{left:140px;top:250px;width:380px;height:380px;border-radius:50% 0 50% 50%;background:radial-gradient(circle at 55% 45%,#c9d6e4 0%,#7d8fa6 45%,#3b4a62 100%)}
.mission-copy{left:578px;top:246px;width:462px;font-size:12.5px;line-height:21.5px;color:#e6ecf5}
.mission-copy p+p{margin-top:12px}

/* since 2015 */
.since-title{left:160px;top:1978px;font-size:36px;line-height:44px;font-weight:400}
.since-copy{left:162px;top:2072px;width:410px;font-size:13.5px;line-height:24.5px;letter-spacing:.3px}
.since-copy p+p{margin-top:4px}
.pill{position:absolute;width:185px;height:225px;border-radius:92px;background:var(--white);box-shadow:0 0 0 6px var(--white),0 0 0 7px var(--ring),0 4px 18px rgba(30,90,140,.1);text-align:center}
.pill-icon{display:block;margin:38px auto 0;width:56px;height:56px}
.pill-num{font-family:"Quicksand",sans-serif;font-size:34px;font-weight:500;color:var(--ink);margin-top:4px}
.pill-label{font-size:13px;line-height:16px;color:var(--text)}

/* testimonials */
.reviews{position:absolute;left:0;top:2525px;width:1200px;height:950px;background:var(--blue);border-radius:0 300px 0 0}
.reviews-title{left:0;width:1200px;top:190px;text-align:center;font-size:34px;color:var(--white);font-weight:400}
.review{position:absolute;top:275px;width:275px;height:465px;border-radius:137px;border:1.5px solid rgba(255,255,255,.55);text-align:center;color:var(--white)}
.review-photo{position:absolute;left:68px;top:28px;width:140px;height:140px;border-radius:50%;background:linear-gradient(160deg,#e8eef3,#b8c6d3)}
.review-name{position:absolute;left:0;right:0;top:212px;font-family:"Quicksand",sans-serif;font-size:23px;font-weight:500}
.review-text{position:absolute;left:26px;right:26px;top:250px;font-size:12.5px;line-height:21.5px}
.slide-arrow{position:absolute;width:36px;height:36px;border-radius:50%;background:var(--navy);display:flex;align-items:center;justify-content:center}

/* faq */
.faq-title{left:0;width:1200px;top:3582px;text-align:center;font-size:34px;font-weight:400}
.faq-item{position:absolute;left:250px;width:698px;background:var(--white);border-radius:6px;box-shadow:0 2px 10px rgba(20,60,110,.14)}
.faq-q{position:absolute;left:12px;top:15px;font-family:"Quicksand",sans-serif;font-size:17px;color:var(--blue);font-weight:600}
.faq-qtext{position:absolute;left:54px;top:10px;width:570px;font-size:12.5px;line-height:18px;color:var(--ink)}
.faq-toggle{position:absolute;right:18px;top:17px;width:22px;height:22px;border-radius:50%;background:var(--navy);display:flex;align-items:center;justify-content:center}
.faq-answer{position:absolute;left:42px;top:72px;width:620px;font-size:12.5px;line-height:22px;color:var(--text)}

/* blog */
.blog-title{left:0;width:1200px;top:4158px;text-align:center;font-size:34px;font-weight:400}
.post{position:absolute;top:4240px;border-radius:12px;overflow:hidden}
.post-caption{position:absolute;left:22px;right:18px;bottom:16px;color:var(--white)}
.post-caption h3{font-family:"Quicksand",sans-serif;font-size:18px;font-weight:600}
.post-caption p{font-size:11.5px;line-height:16px}

/* newsletter & footer */
.signup{position:absolute;left:160px;top:4790px;width:870px;height:200px;background:var(--blue);border-radius:0 100px 100px 0}
.signup-title{left:44px;top:78px;font-size:28px;line-height:34px;color:var(--white);font-weight:400}
.field{position:absolute;top:92px;width:183px;height:38px;border-radius:19px;background:var(--white);font-size:12px;color:var(--ink);padding:12px 18px}
.footer-nav{left:0;width:1200px;top:5078px;display:flex;justify-content:center;gap:26px;font-size:13px;color:#d2dbea}
.footer-contact{top:5178px;font-size:13px;color:var(--white);display:flex;align-items:center;gap:8px;white-space:nowrap}
.bottom-bar{position:absolute;left:0;top:5252px;width:1200px;height:44px;background:var(--blue);font-size:12px;color:var(--white)}
</style>
</head>
<body>

<header class="site-header">
  <div class="brand">
    <span class="brand-mark"></span>
    <div><div class="brand-name">northline</div><div class="brand-sub">CONSULTING</div></div>
  </div>
  <nav class="main-nav"><span>Home</span><span>About Us</span><span>Portfolio</span><span>Contact Us</span><span>Our Services</span><span>Blog</span></nav>
</header>

<section class="hero">
  <div class="photo hero-photo" role="img" aria-label="Doctor in a white coat holding a stethoscope"></div>
  <div class="abs hero-welcome">Welcome to</div>
  <h1 class="abs heading hero-title">NORTHLINE CONSULTING</h1>
  <div class="abs hero-sub">Helping those who help others</div>
  <p class="abs hero-copy">Specialises in helping health professionals&nbsp; like you, stand out from the busy crowd, find new patient and helps you be seen as the go-to person within your industry.</p>
  <div class="btn btn-cyan hero-btn">
    <svg width="18" height="18" viewBox="0 0 24 24" fill="none" stroke="#fff" stroke-width="2" style="margin-right:8px"><path d="M4 20l5-2 10-10a3 3 0 0 0-4-4L5 14z"/></svg>START YOUR PROJECT
  </div>
</section>
<div class="abs scroll-cue"><svg width="18" height="18" viewBox="0 0 24 24" fill="none" stroke="#1fa9e6" stroke-width="2"><path d="M12 4v16M6 14l6 6 6-6"/></svg></div>

<section class="stats">
  <h2 class="abs heading stats-title">DON’T MISS A NEW OPPORTUNITY TO GROW YOU<br>PRACTICE WITH YOUR ONLINE PRESENCE.</h2>
  <p class="abs stats-lead">Being online: a large opportunity for your practice</p>
  <div class="stat-card" style="left:160px"><div class="stat-badge" style="background:var(--blue)">80<sup>%</sup></div><div class="stat-text">of internet uses search<br>for health information</div></div>
  <div class="stat-card" style="left:385px"><div class="stat-badge" style="background:var(--teal)">50<sup>%</sup></div><div class="stat-text">Would like information about a specific health professional</div></div>
  <div class="stat-card" style="left:610px"><div class="stat-badge" style="background:var(--orange)">42<sup>%</sup></div><div class="stat-text">of individuals look at health related consumer reviews</div></div>
  <div class="stat-card" style="left:835px"><div class="stat-badge" style="background:var(--navy)">41<sup>%</sup></div><div class="stat-text">of consumers say online presence may impact their choice of health professional</div></div>
  <div class="btn btn-cyan" style="left:380px;top:454px;width:210px">CONTACT US TODAY</div>
  <div class="btn btn-navy" style="left:612px;top:454px;width:210px">START YOUR PROJECT</div>
</section>

<section class="mission">
  <div class="tint-block" style="left:1064px;top:30px;width:96px;height:90px;background:var(--blue)"></div>
  <div class="tint-block" style="left:1036px;top:48px;width:104px;height:104px;background:rgba(159,182,214,.18)" role="img" aria-label="Decorative dotted panel"></div>
  <h2 class="abs heading mission-title">NORTHLINE CONSULTING HELPING<br>THOSE WHO HELP OTHERS.</h2>
  <div class="photo mission-photo" role="img" aria-label="Doctor using a tablet with a glowing digital health interface"></div>
  <div class="abs mission-copy">
    <p>You became a health professional because you wanted to make a difference and you obviously care about patient outcomes. At first things were great and you had plenty of patients but in the last few years there’s more competition offering the same types of services and products that you do. Regular customers haven’t come back to you in a while and you know you NEED to do something but the old ways like relying on word of mouth doesn’t seem to be working well anymore and you don’t know how to get started.</p>
    <p>But that’s where we can help... Northline Consulting specialises in helping health professionals like you to create a great online user experience for your patients. We help you build your online assets through Website development, social media marketing, Online Traffic Strategies.</p>
  </div>
  <div class="btn btn-cyan" style="left:578px;top:580px;width:210px">CONTACT US TODAY</div>
  <div class="btn btn-white" style="left:810px;top:580px;width:210px">START YOUR PROJECT</div>
</section>

<section>
  <h2 class="abs heading since-title">HELPING<br>CLIENTS SINCE 2015</h2>
  <div class="abs since-copy">
    <p><b style="color:var(--ink)">Northline consulting</b> specialises in helping health professionals&nbsp; like you, stand out from the busy crowd, find new patient and helps you be seen as the go-to person within your industry. Unlike most health professionals who solely rely on word of mouth, we use the latest online marketing techniques to grow you and your practice.</p>
    <p>While our niche has always been in the healthcare industry, Northline Marketing also has experience in providing solutions our e-commerce partners as well as other professional industries.</p>
  </div>
  <div class="btn btn-cyan" style="left:160px;top:2380px;width:210px">CONTACT US TODAY</div>
  <div class="btn btn-navy" style="left:380px;top:2380px;width:210px">START YOUR PROJECT</div>

  <div class="pill" style="left:660px;top:1982px">
    <svg class="pill-icon" viewBox="0 0 56 56" fill="none" stroke="#1b2d52" stroke-width="2.4"><path d="M28 30c-8-6-12-10-12-15a6 6 0 0 1 12-2 6 6 0 0 1 12 2c0 5-4 9-12 15z" fill="#1fa9e6"/><path d="M6 32l10 14h12M50 32L40 46H28"/></svg>
    <div class="pill-num">63%</div><div class="pill-label">Healthcare<br>And Medical</div>
  </div>
  <div class="pill" style="left:856px;top:2086px">
    <svg class="pill-icon" viewBox="0 0 56 56" fill="none" stroke="#1b2d52" stroke-width="2.4"><circle cx="28" cy="18" r="8" fill="#1fa9e6"/><path d="M12 44c0-9 7-15 16-15s16 6 16 15z"/><circle cx="12" cy="22" r="5"/><circle cx="44" cy="22" r="5"/></svg>
    <div class="pill-num">12%</div><div class="pill-label">Other Professional<br>Services</div>
  </div>
  <div class="pill" style="left:670px;top:2226px">
    <svg class="pill-icon" viewBox="0 0 56 56" fill="none" stroke="#1b2d52" stroke-width="2.4"><path d="M4 8h8l6 28h28l5-20H15"/><rect x="24" y="18" width="18" height="12" fill="#1fa9e6"/><circle cx="22" cy="44" r="4"/><circle cx="42" cy="44" r="4"/></svg>
    <div class="pill-num">25%</div><div class="pill-label">Ecommerce<br>Projects</div>
  </div>
</section>

<section class="reviews">
  <div class="tint-block" style="left:550px;top:98px;width:60px;height:60px;background:rgba(255,255,255,.18)" role="img" aria-label="Decorative dotted panel"></div>
  <svg class="abs" style="left:596px;top:100px" width="70" height="64" viewBox="0 0 70 64" fill="#fff"><path d="M4 4h26v28c0 16-8 26-22 30l-3-7c8-3 11-9 11-15H4z"/><path d="M40 4h26v28c0 16-8 26-22 30l-3-7c8-3 11-9 11-15H40z"/></svg>
  <h2 class="abs heading reviews-title">SEE WHAT OUR CLIENTS SAY</h2>
  <div class="slide-arrow" style="left:86px;top:489px"><svg width="14" height="14" viewBox="0 0 24 24" fill="none" stroke="#fff" stroke-width="3"><path d="M15 5l-7 7 7 7"/></svg></div>
  <div class="slide-arrow" style="left:1077px;top:489px"><svg width="14" height="14" viewBox="0 0 24 24" fill="none" stroke="#fff" stroke-width="3"><path d="M9 5l7 7-7 7"/></svg></div>
  <div class="review" style="left:160px"><div class="review-photo" role="img" aria-label="Client portrait"></div><div class="review-name">REMY DALCOURT</div><p class="review-text">“Lorem ipsum dolor sit amet, consectetur adipiscing elit, sed do eiusmod tempor incididunt ut labore et dolore magna aliqua. Ut enim ad minim veniam, quis nostrud exercitation ullamco laboris nisi ut aliquip ex ea commodo consequat.</p></div>
  <div class="review" style="left:462px"><div class="review-photo" role="img" aria-label="Client portrait"></div><div class="review-name">REMY DALCOURT</div><p class="review-text">“Lorem ipsum dolor sit amet, consectetur adipiscing elit, sed do eiusmod tempor incididunt ut labore et dolore magna aliqua. Ut enim ad minim veniam, quis nostrud exercitation ullamco laboris nisi ut aliquip ex ea commodo consequat.</p></div>
  <div class="review" style="left:763px"><div class="review-photo" role="img" aria-label="Client portrait"></div><div class="review-name">REMY DALCOURT</div><p class="review-text">“Lorem ipsum dolor sit amet, consectetur adipiscing elit, sed do eiusmod tempor incididunt ut labore et dolore magna aliqua. Ut enim ad minim veniam, quis nostrud exercitation ullamco laboris nisi ut aliquip ex ea commodo consequat.</p></div>
  <div class="btn btn-navy" style="left:378px;top:785px;width:210px">CONTACT US TODAY</div>
  <div class="btn btn-white" style="left:610px;top:785px;width:210px">START YOUR PROJECT</div>
</section>

<section>
  <div class="tint-block" style="left:74px;top:3556px;width:96px;height:96px;background:#bfe6f8"></div>
  <div class="tint-block" style="left:48px;top:3582px;width:102px;height:106px;background:rgba(75,159,214,.12)" role="img" aria-label="Decorative dotted panel"></div>
  <h2 class="abs heading faq-title">FREQUENTLY ASKED QUESTIONS</h2>
  <div class="faq-item" style="top:3652px;height:200px">
    <span class="faq-q">Q.1</span>
    <p class="faq-qtext">Lorem ipsum dolor sit amet, consectetur adipiscing elit, sed do eiusmod tempor incididunt ut labore et dolore magna aliqua. Lorem ipsum dolor</p>
    <span class="faq-toggle" style="background:var(--blue)"><svg width="10" height="10" viewBox="0 0 24 24" fill="none" stroke="#fff" stroke-width="4"><path d="M5 15l7-7 7 7"/></svg></span>
    <p class="faq-answer">“Lorem ipsum dolor sit amet, consectetur adipiscing elit, sed do eiusmod incididunt labore et dolore magna aliqua. Ut enim ad minim veniam, quis nostrud exercitation ullamco laboris nisi ut aliquip ex ea commodo consequat. Duis aute irure dolor in reprehenderit in voluptate velit esse cillum dolore eu fugiat nulla pariatur. Excepteur sint occaecat cupidatat non proident, sunt in culpa qui officia deserunt mollit anim id est laborum.”</p>
  </div>
  <div class="faq-item" style="top:3878px;height:56px"><span class="faq-q">Q.2</span><p class="faq-qtext">Sit amet, consectetur adipiscing elit, sed do eiusmod tempor incididunt ut labore et dolore magna aliqua.&nbsp; velit esse cillum</p><span class="faq-toggle"><svg width="10" height="10" viewBox="0 0 24 24" fill="none" stroke="#fff" stroke-width="4"><path d="M5 9l7 7 7-7"/></svg></span></div>
  <div class="faq-item" style="top:3952px;height:56px"><span class="faq-q">Q.3</span><p class="faq-qtext">Dipiscing elit, sed do eiusmod tempor Lorem ipsum dolor sit amet, consectetur a incididunt ut labore et dolore magna aliqua.&nbsp; velit esse cillum</p><span class="faq-toggle"><svg width="10" height="10" viewBox="0 0 24 24" fill="none" stroke="#fff" stroke-width="4"><path d="M5 9l7 7 7-7"/></svg></span></div>
  <div class="faq-item" style="top:4024px;height:56px"><span class="faq-q">Q.4</span><p class="faq-qtext">Dipiscing elit, sed do eiusmod tempor Lorem ipsum dolor sit amet, consectetur a incididunt ut labore et dolore magna aliqua.</p><span class="faq-toggle"><svg width="10" height="10" viewBox="0 0 24 24" fill="none" stroke="#fff" stroke-width="4"><path d="M5 9l7 7 7-7"/></svg></span></div>
</section>

<section>
  <h2 class="abs heading blog-title">BLOG POSTS</h2>
  <article class="post" style="left:162px;width:416px;height:355px;background:linear-gradient(150deg,#4a6a9a 0%,#c9a88a 55%,#8a6a55 100%)" role="img" aria-label="Designer sketching website wireframes at a desk">
    <div class="post-caption"><h3>Lorem Ipsum is simply dummy</h3><p>Lorem Ipsum is simply dummy text of the printing ad typesetting industry. Lorem Ipsum has been</p></div>
  </article>
  <article class="post" style="left:600px;width:208px;height:300px;background:linear-gradient(160deg,#d6dde3 0%,#9aa4ad 60%,#5e6a75 100%)" role="img" aria-label="Hand holding a smartphone">
    <div class="post-caption" style="left:18px"><p>Lorem Ipsum is text of the printing ad typesetting</p></div>
  </article>
  <article class="post" style="left:832px;width:206px;height:300px;background:linear-gradient(160deg,#e6f0f7 0%,#8fb3d6 55%,#3d6a9a 100%)" role="img" aria-label="Laptop showing a medical website">
    <div class="post-caption" style="left:18px"><p>Lorem Ipsum is text of the printing ad typesetting</p></div>
  </article>
  <div class="abs" style="left:784px;top:4540px;width:64px;height:32px;background:var(--white);border-radius:4px;display:flex;justify-content:space-around;align-items:center">
    <svg width="12" height="12" viewBox="0 0 24 24" fill="none" stroke="#1fa9e6" stroke-width="3"><path d="M15 5l-7 7 7 7"/></svg>
    <svg width="12" height="12" viewBox="0 0 24 24" fill="none" stroke="#1fa9e6" stroke-width="3"><path d="M9 5l7 7-7 7"/></svg>
  </div>
  <div class="btn btn-cyan" style="left:553px;top:4632px;width:150px">VIEW ALL</div>
  <div class="photo" style="left:900px;top:4575px;width:290px;height:220px;border-radius:50%;background:radial-gradient(circle at 60% 45%,#f2d3d3 0%,#d9dfe6 45%,rgba(255,255,255,0) 72%)" role="img" aria-label="Piggy bank with a stethoscope"></div>
</section>

<footer>
  <svg class="abs" style="left:0;top:4700px" width="1200" height="596" viewBox="0 0 1200 596"><path d="M0 200C60 90 180 40 300 40H1200V596H0Z" fill="#15244a"/></svg>
  <div class="signup">
    <div class="abs" style="left:6px;top:0;width:72px;height:36px;background:var(--orange);border-radius:0 0 36px 36px"></div>
    <h2 class="abs heading signup-title">SIGN UP TO OUR<br>MAILING LIST</h2>
    <div class="field" style="left:312px">Name</div>
    <div class="field" style="left:512px">Email</div>
    <div class="btn btn-navy" style="left:712px;top:92px;width:133px;height:38px;font-size:11.5px">SIGN UP NOW</div>
  </div>
  <div class="abs" style="left:586px;top:4976px;width:28px;height:28px;border-radius:50%;background:var(--teal)"></div>
  <nav class="abs footer-nav"><span>Home</span><span>|</span><span>About</span><span>|</span><span>Portfolio</span><span>|</span><span>Contact Us</span><span>|</span><span>Our Services</span><span>|</span><span>Blog</span></nav>
  <div class="abs footer-contact" style="left:160px">
    <svg width="16" height="12" viewBox="0 0 16 12" fill="none" stroke="#fff" stroke-width="1.5"><rect x="1" y="1" width="14" height="10"/><path d="M1 1l7 6 7-6"/></svg>
    EMAIL :&nbsp; inquiry@northline.example
  </div>
  <div class="abs" style="left:452px;top:5168px;width:1px;height:36px;background:#8fa3c4"></div>
  <div class="abs footer-contact" style="left:474px"><span style="width:24px;height:24px;border-radius:50%;background:var(--blue)"></span>Facenet</div>
  <div class="abs footer-contact" style="left:616px"><span style="width:24px;height:24px;border-radius:50%;background:var(--blue)"></span>Photogram</div>
  <div class="abs" style="left:744px;top:5168px;width:1px;height:36px;background:#8fa3c4"></div>
  <div class="abs" style="left:798px;top:5172px;display:flex;align-items:center;gap:8px"><span style="width:26px;height:26px;border-radius:50%;background:var(--blue)"></span><span class="brand-name" style="font-size:26px">northline</span></div>
  <div class="bottom-bar">
    <span class="abs" style="left:160px;top:15px">© 2022 Northline Consulting . All Rights Reserved.</span>
    <span class="abs" style="left:742px;top:15px">Terms and Conditions&nbsp; |&nbsp; Privacy policy</span>
  </div>
</footer>

</body>
</html>
```